Trifold brochure for Thai yoga massage practice (In a Combat gym and a Spa)

I am a Practitioner of Thai massage in Toronto, and will in the near future be offering personal training with transitional fitness from couch potato to weekend warriors.

I train in Muay-thai and my current stream of clients are "thai tigers" in need of restorative therapy to get them back on their feet - hence the website name Ravenhush.com.
My other stream of clients are in a Lovely Spa on a rooftop patio (if you're ever in Toronto come on by).

So I have the best of two worlds (injuries vs. pure bliss) Dark vs. Light

I want to introduce Thai yoga massage to a new modern audience. Thai massage is an ancient, effective hybrid therapy incorporating traditional acupressure/ body meridian therapy and human kinetics simultaneously.

Brochures are meant for distribution to martial arts studios, fitness gyms and other spas.

I am open to eye-catching, out of the box ideas.

My website: www.ravenhush.com (I am in the process of editing this new web space - apologies for the very basic nature of it)

Pictures are attached for review or view my link:
https://files.pelorandrop.net/share?id=7Xq41mPbR2kLwZt9VhDs&ref=open

Thank you!

Target Market(s)

20-45 year old fitness enthusiast for a gym audience
or 20-55 year old looking for general wellness/ relaxation
or combination of both (yin/yang type design)

Industry/Entity Type

Training

Font styles to use
Decorative

Requirements
Must have
• Will be looking for innovation, clever, witty design, please be creative. Toronto is a quirky city, I welcome quirky, yet tasteful designs.

Please use a good amount of flow, and streaming lines.
Nice to have
• If we could have a yin / yang effect that would be nice (Combat restoration vs. Relaxation)
Should not have
• Please do not have text / designs that convey the stereotypical nonsense that surround Asian based massage (my cup is full already).

```html
<!DOCTYPE html>
<html lang="en">
<head>
<meta charset="utf-8">
<title>Raven Hush – Thai Yoga Massage Trifold</title>
<link rel="stylesheet" href="https://fonts.googleapis.com/css2?family=Open+Sans:wght@400;600&family=Noto+Sans:wght@400;700&display=swap">
<style>
  :root {
    --backdrop: #9c9c9c;
    --paper: #f7f6f5;
    --band-brown: #a89080;
    --band-light: #d9cbc1;
    --text-brown: #8c6c56;
    --text-grey: #8a8a8a;
    --body-ink: #2b2b2b;
    --badge-blue: #5fb1e0;
    --badge-ring: #9fd0ec;
    --map-blue: #c2e5f7;
  }
  * { box-sizing: border-box; margin: 0; padding: 0; }
  html, body { width: 1200px; height: 704px; overflow: hidden; }
  body {
    background: radial-gradient(ellipse at 50% 40%, #b4b4b4 0%, var(--backdrop) 100%);
    font-family: "Noto Sans", sans-serif;
    position: relative;
  }
  .brochure {
    position: absolute;
    left: 60px; top: 72px;
    width: 1080px; height: 560px;
    background: var(--paper);
    box-shadow: 0 14px 30px rgba(0,0,0,.28);
  }
  .bands { position: absolute; inset: 0; }
  .fold {
    position: absolute; top: 0; bottom: 0; width: 1px;
    background: rgba(0,0,0,.08);
  }
  .fold--first { left: 360px; }
  .fold--second { left: 720px; }

  .photo {
    position: absolute;
    background: linear-gradient(135deg, #6e6a66 0%, #b9aca0 55%, #e2dcd6 100%);
  }
  .photo--session { left: 24px; top: 72px; width: 310px; height: 166px; }
  .photo--stretch {
    left: 720px; top: 34px; width: 360px; height: 226px;
    background: linear-gradient(160deg, #2a2a2a 0%, #4b3a3a 40%, #b8332f 60%, #5a4f9a 85%, #8f8f8f 100%);
  }

  .feature-heading {
    position: absolute; left: 40px; top: 248px; width: 200px;
    font-family: "Open Sans", sans-serif; font-weight: 400;
    font-size: 20px; line-height: 22px; color: var(--text-brown);
  }
  .feature-body {
    position: absolute; left: 40px; top: 300px; width: 280px;
    font-size: 13.5px; line-height: 17px; color: var(--body-ink);
  }

  .badge {
    position: absolute; width: 124px; height: 124px; border-radius: 50%;
    background: var(--badge-ring);
    display: flex; align-items: center; justify-content: center;
  }
  .badge__inner {
    width: 104px; height: 104px; border-radius: 50%;
    background: var(--badge-blue);
    display: flex; flex-direction: column; align-items: center; justify-content: center;
    text-align: center; padding: 0 8px;
  }
  .badge__label { font-size: 7.5px; font-weight: 700; color: #fff; line-height: 9px; }
  .badge__text { font-size: 8px; font-weight: 700; color: #111; line-height: 10px; margin-top: 2px; }
  .badge--one { left: 20px; top: 416px; }
  .badge--two { left: 186px; top: 436px; }

  .brand {
    position: absolute; left: 360px; top: 70px; width: 360px; text-align: center;
  }
  .brand__mark {
    width: 96px; height: 80px; margin: 0 auto;
    background: linear-gradient(135deg, #ececec, #d0d0d0);
  }
  .brand__name {
    margin-top: 8px;
    font-family: "Open Sans", sans-serif; font-size: 20px; letter-spacing: 1px;
    color: var(--text-grey);
  }
  .world-map {
    position: absolute; left: 410px; top: 200px; width: 260px; height: 130px;
    background: radial-gradient(ellipse at 50% 50%, var(--map-blue) 0%, #d9f0fb 60%, rgba(217,240,251,0) 100%);
  }
  .contact {
    position: absolute; left: 360px; top: 350px; width: 360px; text-align: center;
    font-family: "Open Sans", sans-serif; font-style: normal;
    font-size: 13px; line-height: 16px; color: var(--text-grey);
  }
  .contact__mail { margin-top: 22px; }

  .title-block {
    position: absolute; left: 720px; top: 284px; width: 360px; padding-left: 50px;
  }
  .title-block::before {
    content: ""; position: absolute; left: 0; top: -4px; width: 10px; height: 66px;
    background: var(--band-light);
  }
  .title-block__name {
    font-family: "Open Sans", sans-serif; font-weight: 600; font-size: 23px;
    color: var(--text-brown); text-align: right; padding-right: 34px;
  }
  .title-block__tagline {
    margin-top: 6px; font-family: "Open Sans", sans-serif; font-size: 11.5px;
    color: #a99484; text-align: right; padding-right: 34px;
  }
  .web-address {
    position: absolute; right: 28px; bottom: 22px;
    font-family: "Open Sans", sans-serif; font-size: 13px; color: #ece3dc;
  }
</style>
</head>
<body>
<main class="brochure">
  <svg class="bands" width="1080" height="560" viewBox="0 0 1080 560" aria-hidden="true">
    <path d="M0 0 H1080 V20 L720 14 L360 44 L0 56 Z" fill="var(--band-brown)"/>
    <path d="M0 56 L360 44 L720 14 L1080 20 V34 L720 28 L360 54 L0 66 Z" fill="var(--band-light)"/>
    <path d="M0 430 C120 410 240 390 360 470 C480 480 600 440 720 416 C840 400 960 400 1080 392 V560 H0 Z" fill="var(--band-light)"/>
    <path d="M0 442 C120 424 240 406 360 484 C480 494 600 456 720 430 C840 414 960 412 1080 404 V560 H0 Z" fill="var(--band-brown)"/>
  </svg>
  <div class="fold fold--first"></div>
  <div class="fold fold--second"></div>

  <section class="panel panel--inside">
    <div class="photo photo--session" role="img" aria-label="Photo of a practitioner giving a Thai massage to a client lying on a mat"></div>
    <h2 class="feature-heading">Here goes your heading, make it</h2>
    <p class="feature-body">Here goes your headingEscipit ea ere sinctem que non et optaquidiae volorecte quodi dia voluptat haribus eligentur reped quid qui omnia sedicip sandem se exere ea alisim quas dolupta qui consed unt.</p>
    <div class="badge badge--one"><div class="badge__inner">
      <span class="badge__label">THIS IS IMPORTANT</span>
      <span class="badge__text">Here goes your headingEscipit ea ere sinctem que non et optaquidiae volorecte quodi.</span>
    </div></div>
    <div class="badge badge--two"><div class="badge__inner">
      <span class="badge__label">THIS IS IMPORTANT</span>
      <span class="badge__text">Here goes your headingEscipit ea ere sinctem que non et optaquidiae volorecte quodi.</span>
    </div></div>
  </section>

  <section class="panel panel--back">
    <div class="brand">
      <div class="brand__mark" role="img" aria-label="Illustration of a leaping striped big cat"></div>
      <p class="brand__name">RAVEN HUSH</p>
    </div>
    <div class="world-map" role="img" aria-label="Light blue world map"></div>
    <address class="contact">
      <p>Lindqvist ulica br 42.</p>
      <p>00387 61 208 394</p>
      <p>00387 61 55 70 12</p>
      <p class="contact__mail">mail@pelorstudio.com</p>
    </address>
  </section>

  <section class="panel panel--cover">
    <div class="photo photo--stretch" role="img" aria-label="Photo of a practitioner in red guiding a leg stretch for a client on a purple mat in a gym"></div>
    <div class="title-block">
      <h1 class="title-block__name">Thai Yoga Massage</h1>
      <p class="title-block__tagline">Restore Your Inner Beast</p>
    </div>
    <p class="web-address">www.pelorstudio.com</p>
  </section>
</main>
</body>
</html>
```